Quarrytide Hosting - Direct Mailer / Flyer

We are excited to announce the launch of our new company, Quarrytide Hosting, a premier cohosting facility and data center dedicated to Cryptocurrency Miners. Our website, https://quarrytidehosting.example, provides detailed information about our offerings and showcases the innovative design schemes for the entire project.

Quarrytide Hosting stands out in the industry by offering both GPU Hosting and ASIC Hosting services in our state-of-the-art facility, equipped with an impressive 17 Megawatts of available power. What sets us apart is our unique billing system based on actual metered power usage. We charge $0.08 for ASIC miners and $0.09 for GPU miners, ensuring cost-effectiveness and transparency for our clients.

Our commitment to excellence is evident in our use of cutting-edge technology, top-notch facilities, and strategic partnerships. These elements come together to deliver exceptional solutions tailored for real-world applications in the cryptocurrency space.

As part of our promotional efforts, we are developing a direct mailer/flyer to introduce Quarrytide Hosting to a wider audience. This promotional material will also serve as a handout at events, to potential customers, and more. We welcome creative ideas and suggestions to maximize the versatility of this design and reach diverse target audiences effectively.

For a comprehensive overview of our services and to explore our design concepts, please visit https://quarrytidehosting.example. Quarrytide Hosting is poised to revolutionize the mining industry, and we look forward to partnering with you for success in the digital currency era.

```html
<!DOCTYPE html>
<html lang="en">
<head>
<meta charset="utf-8">
<title>Quarrytide Hosting – Flyer</title>
<link href="https://fonts.googleapis.com/css2?family=Poppins:wght@400;500;600;700;800&display=swap" rel="stylesheet">
<style>
:root{
  --blue:#3b55f5;
  --blue-deep:#2f46e0;
  --ink:#0d0d12;
  --white:#ffffff;
  --stat-blue-bg:#e4e7f6;
  --stat-green-bg:#e3f0e8;
  --green:#1f9a2a;
  --photo-dark:#0b1b2c;
  --photo-glow:#1c6d86;
}
*{margin:0;padding:0;box-sizing:border-box}
html,body{width:703px;height:1200px;overflow:hidden;background:var(--white)}
body{font-family:"Poppins",sans-serif;color:var(--ink);position:relative}
.flyer{position:relative;width:703px;height:1200px;overflow:hidden;background:var(--white)}
.hero-art{position:absolute;left:0;top:0;width:703px;height:420px}
.brand{position:absolute;left:17px;top:28px;display:flex;align-items:center;gap:8px;font-weight:800;font-size:18px;color:var(--ink);letter-spacing:.2px}
.brand-square{width:18px;height:18px;background:var(--ink)}
.headline{position:absolute;left:38px;top:118px;line-height:1;font-weight:700}
.headline .l1{font-size:44px;display:block}
.headline .l2{font-size:48px;color:var(--blue);font-weight:800;display:block;margin-top:2px}
.headline .l2 small{font-size:28px;color:var(--ink);font-weight:700;margin-left:6px}
.headline .l3{font-size:52px;font-weight:800;display:block;margin-top:2px}
.tagline{position:absolute;left:82px;top:310px;width:250px;font-size:14px;font-weight:500;line-height:1.3}
.solutions{position:absolute;left:0;top:440px;width:703px;text-align:center}
.solutions h2{font-size:35px;font-weight:700;line-height:1.05}
.solutions p{width:520px;margin:12px auto 0;font-size:11px;font-weight:500;line-height:1.45}
.services-band{position:absolute;left:0;top:659px;width:703px;height:321px;background:linear-gradient(180deg,var(--blue) 0%,var(--blue-deep) 100%)}
.stat{position:absolute;top:607px;width:219px;height:126px;border:1.5px dashed #333;border-radius:10px;text-align:center;padding-top:12px}
.stat svg{width:36px;height:36px}
.stat strong{display:block;font-size:24px;font-weight:700;line-height:1.1;margin-top:4px}
.stat span{display:block;font-size:11.5px;font-weight:500;line-height:1.2}
.stat-watts{left:103px;background:var(--stat-blue-bg)}
.stat-watts strong{color:var(--blue)}
.stat-green{left:366px;background:var(--stat-green-bg)}
.stat-green strong{color:var(--green)}
.services-title{position:absolute;top:750px;width:703px;text-align:center;color:var(--white);font-size:30px;font-weight:600}
.services{position:absolute;top:818px;left:36px;width:632px;display:flex;color:var(--white);text-align:center}
.service{flex:1;padding:0 8px;border-left:1px solid rgba(255,255,255,.35)}
.service:first-child{border-left:none}
.service svg{width:24px;height:24px}
.service h3{font-size:15px;font-weight:600;margin-top:4px}
.service p{font-size:11px;line-height:1.3;margin-top:6px}
.needs-title{position:absolute;top:990px;width:703px;text-align:center;color:var(--blue);font-size:24px;font-weight:600}
.features{position:absolute;top:1042px;left:58px;display:grid;grid-template-columns:180px 204px 230px;row-gap:13px}
.feature{display:flex;align-items:center;gap:12px;font-size:14px;font-weight:600}
.feature svg{width:18px;height:18px;flex:none}
.footer-art{position:absolute;left:0;top:1120px;width:703px;height:80px}
.phone{position:absolute;left:40px;top:1146px;display:flex;align-items:center;gap:10px;font-size:19px;font-weight:700}
.phone svg{width:18px;height:26px}
.contacts{position:absolute;left:296px;right:14px;top:1153px;display:flex;justify-content:space-between;color:var(--white);font-size:9.5px;font-weight:500;white-space:nowrap}
.contacts div{display:flex;align-items:center;gap:6px}
.contacts svg{width:14px;height:14px;flex:none}
</style>
</head>
<body>
<main class="flyer">
  <svg class="hero-art" viewBox="0 0 703 420">
    <defs>
      <linearGradient id="photoTone" x1="0" y1="0" x2="1" y2="1">
        <stop offset="0" stop-color="#13263a"/>
        <stop offset=".5" stop-color="#1c6d86"/>
        <stop offset="1" stop-color="#0b1b2c"/>
      </linearGradient>
    </defs>
    <polygon points="236,0 256,0 446,300 446,420 432,420 432,306" fill="#3b55f5"/>
    <polygon role="img" aria-label="Photo of glowing server racks with a cloud symbol in a data center" points="256,0 703,0 703,420 449,420 449,298" fill="url(#photoTone)"/>
    <polygon points="0,256 58,322 58,420 0,420" fill="#3b55f5"/>
    <polygon points="0,236 74,318 74,420 66,420 66,322 0,248" fill="#3b55f5"/>
  </svg>

  <div class="brand"><span class="brand-square"></span>Quarrytide Hosting</div>

  <h1 class="headline">
    <span class="l1">Transform</span>
    <span class="l2">MINING<small>With</small></span>
    <span class="l3">Cohosting</span>
  </h1>
  <p class="tagline">Miners deserve the best - choose the hosting company that delivers excellence!</p>

  <section class="solutions">
    <h2>Real Solutions<br>For Real Applications</h2>
    <p>Quarrytide Hosting has committed to leveraging cutting-edge technology, state-of-the-art facilities, and strategic partnerships to deliver exceptional solutions tailored for real-world applications in the cryptocurrency space.</p>
  </section>

  <div class="services-band"></div>

  <div class="stat stat-watts">
    <svg viewBox="0 0 36 36" fill="none" stroke="#3b55f5" stroke-width="2"><rect x="4" y="4" width="28" height="22" rx="2"/><line x1="4" y1="11" x2="32" y2="11"/><line x1="9" y1="16" x2="27" y2="16"/><line x1="9" y1="21" x2="22" y2="21"/><line x1="18" y1="26" x2="18" y2="32"/><line x1="11" y1="32" x2="25" y2="32"/></svg>
    <strong>4,000,000+</strong>
    <span>watts available for hosting</span>
  </div>
  <div class="stat stat-green">
    <svg viewBox="0 0 36 36" fill="none" stroke="#1f9a2a" stroke-width="2"><circle cx="18" cy="18" r="14"/><ellipse cx="18" cy="18" rx="6" ry="14"/><line x1="4" y1="18" x2="32" y2="18"/></svg>
    <strong>2,000,000+</strong>
    <span>watts of green energy<br>being produced</span>
  </div>

  <h2 class="services-title">Our Services</h2>
  <section class="services">
    <div class="service">
      <svg viewBox="0 0 24 24" fill="none" stroke="#fff" stroke-width="1.6"><circle cx="12" cy="12" r="11"/><rect x="7" y="7" width="10" height="10"/></svg>
      <h3>GPU Hosting</h3>
      <p>Begin your GPU Hosting journey with rates starting at $0.09 kWh, accepting all equipment.</p>
    </div>
    <div class="service">
      <svg viewBox="0 0 24 24" fill="none" stroke="#fff" stroke-width="1.6"><circle cx="12" cy="12" r="11"/><rect x="7" y="7" width="10" height="10"/><line x1="7" y1="12" x2="17" y2="12"/></svg>
      <h3>ASIC Hosting</h3>
      <p>Get your ASICs directly from us or send yours in today, starting at an all-in rate of $0.08 kWh.</p>
    </div>
    <div class="service">
      <svg viewBox="0 0 24 24" fill="none" stroke="#fff" stroke-width="1.6"><circle cx="12" cy="12" r="11"/><circle cx="12" cy="12" r="5"/></svg>
      <h3>Mining Hardware</h3>
      <p>Looking for mining hardware? Our equipment comes with no additional markup, ever.</p>
    </div>
    <div class="service">
      <svg viewBox="0 0 24 24" fill="none" stroke="#fff" stroke-width="1.6"><circle cx="12" cy="12" r="11"/><circle cx="12" cy="9" r="3"/><path d="M6 18c1-3 3-4 6-4s5 1 6 4"/></svg>
      <h3>Crypto Consulting</h3>
      <p>Enjoy complete White Glove Services for setup, insurance, and tax consulting.</p>
    </div>
  </section>

  <h2 class="needs-title">Hosting Tailored To Your Needs</h2>
  <section class="features">
    <div class="feature"><svg viewBox="0 0 18 18" fill="none" stroke="#3b55f5" stroke-width="1.5"><path d="M10 1 4 10h5l-1 7 6-9H9z"/></svg>99.45% Uptime</div>
    <div class="feature"><svg viewBox="0 0 18 18" fill="none" stroke="#3b55f5" stroke-width="1.5"><rect x="3" y="2" width="12" height="14" rx="1"/><line x1="3" y1="7" x2="15" y2="7"/><line x1="3" y1="11" x2="15" y2="11"/></svg>Advanced Security</div>
    <div class="feature"><svg viewBox="0 0 18 18" fill="none" stroke="#3b55f5" stroke-width="1.5"><rect x="2" y="9" width="6" height="7"/><rect x="10" y="5" width="6" height="11"/><rect x="6" y="1" width="6" height="6"/></svg>Large Facility Capacity</div>
    <div class="feature"><svg viewBox="0 0 18 18" fill="none" stroke="#3b55f5" stroke-width="1.5"><path d="M3 11V9a6 6 0 0 1 12 0v2"/><rect x="2" y="10" width="3" height="5" rx="1"/><rect x="13" y="10" width="3" height="5" rx="1"/></svg>Expert Support</div>
    <div class="feature"><svg viewBox="0 0 18 18" fill="none" stroke="#3b55f5" stroke-width="1.5"><circle cx="9" cy="9" r="7"/><path d="M9 4v5l3 2"/></svg>Metered Usage</div>
    <div class="feature"><svg viewBox="0 0 18 18" fill="none" stroke="#3b55f5" stroke-width="1.5"><circle cx="8" cy="6" r="3.5"/><path d="M2 16c1-4 3-5 6-5s4 1 5 2"/><path d="M12 15l2 1 3-4"/></svg>Direct Equipment Access</div>
  </section>

  <svg class="footer-art" viewBox="0 0 703 80" aria-hidden="true">
    <polygon points="236,0 703,0 703,80 280,80 280,44" fill="#3b55f5"/>
    <polygon points="218,0 228,0 272,40 272,80 264,80 264,44" fill="#3b55f5"/>
  </svg>

  <div class="phone">
    <svg viewBox="0 0 18 26" fill="none" stroke="#3b55f5" stroke-width="1.8"><rect x="2" y="1" width="14" height="24" rx="2"/><line x1="7" y1="21" x2="11" y2="21"/></svg>
    91+-000 555 0142
  </div>
  <div class="contacts">
    <div><svg viewBox="0 0 16 16" fill="none" stroke="#fff" stroke-width="1.4"><rect x="1" y="3" width="14" height="10"/><path d="M1 3l7 6 7-6"/></svg>hello@quarrytidehosting.example</div>
    <div><svg viewBox="0 0 16 16" fill="none" stroke="#fff" stroke-width="1.4"><circle cx="8" cy="8" r="7"/><ellipse cx="8" cy="8" rx="3" ry="7"/><line x1="1" y1="8" x2="15" y2="8"/></svg>www.quarrytidehosting.example</div>
  </div>
</main>
</body>
</html>
```